Storm Restoration Contractor needs a professional business card design

Looking for a professional business card design. Not looking for your cheapo MS Word standard ones that are readily available. Dont want it to be cookie cutter look like ones readily available online. We just recently changed our logo and want to freshen up all our documents. Our company handles restoring a property back to a pre-loss condition after a storm damages it. For example, wind, hail, flood, fire losses.

Target Market(s)

Property Owners, Homeowners, Property Owners, Commercial Property Owners, Property Management Companies, Hail and Wind Damaged Properties

Industry/Entity Type

Construction Company

Contact Information for Business Card

Brightline Facades
847-555-0193
847-555-0147 fax
www.brightlinefacades.example
info@brightlinefacades.example

Requirements
Must have
• Clean, Professional, fresh look
• Storm Restoration, Roofing, Siding, Windows
Nice to have
• If there is a way to incorporate storms that may be cool.

```html
<!DOCTYPE html>
<html lang="en">
<head>
<meta charset="utf-8">
<title>Brightline Facades – Business Card</title>
<link rel="stylesheet" href="https://fonts.googleapis.com/css2?family=Orbitron:wght@600;700&family=Roboto:wght@400&display=swap">
<style>
  :root {
    --page-bg: #e4e2df;
    --card-bg: #f7f8f9;
    --brand-blue: #1f7fb8;
    --deep-blue: #16689c;
    --charcoal: #3d4146;
    --text-grey: #4a4e53;
    --service-text: #eef5fa;
  }
  * { margin: 0; padding: 0; box-sizing: border-box; }
  html, body { width: 1200px; height: 1200px; overflow: hidden; }
  body {
    background: var(--page-bg);
    font-family: "Roboto", Arial, sans-serif;
    position: relative;
  }
  .business-card {
    position: absolute;
    left: 75px; top: 300px;
    width: 1050px; height: 600px;
    background: var(--card-bg);
    border-radius: 6px;
    overflow: hidden;
    box-shadow: 0 10px 30px rgba(0,0,0,0.15);
  }
  .card-waves { position: absolute; inset: 0; }
  .holder {
    position: absolute; left: 50px; top: 95px;
  }
  .holder-name {
    font-family: "Orbitron", "Arial Black", sans-serif;
    font-weight: 700;
    font-size: 34px;
    letter-spacing: 3px;
    color: var(--brand-blue);
  }
  .holder-title {
    margin-top: 8px;
    font-size: 23px;
    color: var(--text-grey);
  }
  .brand {
    position: absolute; right: 58px; top: 88px;
    display: flex; align-items: center; gap: 20px;
  }
  .brand-dot {
    width: 92px; height: 92px; border-radius: 50%;
    background: var(--brand-blue);
  }
  .brand-name {
    font-family: "Orbitron", "Arial Black", sans-serif;
    font-weight: 700;
    font-size: 40px;
    line-height: 1.08;
    color: var(--brand-blue);
    letter-spacing: 1px;
  }
  .contact-list {
    position: absolute; left: 50px; top: 310px;
    list-style: none;
  }
  .contact-item {
    display: flex; align-items: center;
    height: 41px;
    font-size: 25px;
    color: var(--text-grey);
  }
  .contact-item svg { width: 26px; height: 26px; margin-right: 26px; fill: var(--brand-blue); }
  .contact-item .web { color: var(--brand-blue); }
  .service-list {
    position: absolute; right: 55px; top: 420px;
    list-style: none; text-align: right;
  }
  .service-item {
    height: 41px;
    font-size: 25px;
    color: var(--service-text);
  }
  .service-item::after { content: "«"; margin-left: 18px; }
</style>
</head>
<body>
  <section class="business-card">
    <svg class="card-waves" viewBox="0 0 1050 600" preserveAspectRatio="none" aria-hidden="true">
      <path fill="var(--brand-blue)" d="M0,545 C230,600 420,530 560,440 C700,350 860,322 1050,308 L1050,600 L0,600 Z"/>
      <path fill="var(--deep-blue)" opacity="0.35" d="M0,580 C260,610 470,540 620,460 C760,390 900,360 1050,350 L1050,600 L0,600 Z"/>
      <path fill="var(--charcoal)" d="M0,505 C220,548 390,520 520,430 C650,345 830,300 1050,282 L1050,296 C840,312 680,360 545,440 C410,522 230,560 0,525 Z"/>
      <path fill="var(--charcoal)" opacity="0.85" d="M110,500 C260,540 420,520 540,455 C430,540 260,555 110,500 Z"/>
    </svg>

    <div class="holder">
      <h1 class="holder-name">DANIEL REYES</h1>
      <p class="holder-title">Managing Director</p>
    </div>

    <div class="brand">
      <span class="brand-dot"></span>
      <p class="brand-name">BRIGHTLINE<br>FACADES</p>
    </div>

    <ul class="contact-list">
      <li class="contact-item">
        <svg viewBox="0 0 24 24"><path d="M3 8c0-2 3-4 9-4s9 2 9 4v2h-5V8H8v2H3zM6 11h12l2 8H4z"/></svg>
        847-555-0193
      </li>
      <li class="contact-item">
        <svg viewBox="0 0 24 24"><path d="M7 3h10v5H7zM3 9h18v8h-3v4H6v-4H3zM8 14v5h8v-5z"/></svg>
        847-555-0147 fax
      </li>
      <li class="contact-item">
        <svg viewBox="0 0 24 24"><path d="M2 5h20v14H2zM4 7v1l8 5 8-5V7l-8 5z"/></svg>
        info@brightlinefacades.example
      </li>
      <li class="contact-item">
        <svg viewBox="0 0 24 24"><path d="M12 2a10 10 0 1 0 0 20 10 10 0 0 0 0-20zm0 2c1 1 2 3 2.3 6H9.7C10 7 11 5 12 4zM4.1 11h3.6c.1 2 .5 4 1.3 5.5A8 8 0 0 1 4.1 13zm12.2 0h3.6v2a8 8 0 0 1-4.9 3.5c.8-1.5 1.2-3.5 1.3-5.5zM9.7 12h4.6c-.2 3-1.2 5-2.3 6-1.1-1-2.1-3-2.3-6z"/></svg>
        <span class="web">brightlinefacades.example</span>
      </li>
    </ul>

    <ul class="service-list">
      <li class="service-item">Siding</li>
      <li class="service-item">Roofing</li>
      <li class="service-item">Windows</li>
      <li class="service-item">Storm Restoration</li>
    </ul>
  </section>
</body>
</html>
```